Thibodeau Bayou

I am launching a new Cajun Steakhouse.
We have purchased a food truck to support the restaurant and sell some our food until the opening in March. 2025. The truck has a white blank canvas on all sides. The right side has multiple raised surfaces (Serving widow,, TV enclosure with speakers, pop up fold-down service table. There is a sliding door on the right with two windows. The bottom window will be covered in wrap. The primary color will be black. Need a bold and fresh design. A Look that will stand out but not be over the top. The truck is a 18’ Ironmule truck (QSD Trick). I have included pictures of the truck, our logo, some pictures of some of the meals that will be served from the truck, a picture of our already branded catering truck, and various other promotional branding we use. The Food truck doesn’t have to look exactly like our catering truck, but I want to keep the black background with our colorful logo. Everything else is can be created.
Our specialty is Garlic Dungenes Crab and that needs to be highlighted (The Best in the Bay).

Target Market(s)

General Public

Industry/Entity Type

Food Service

Font styles to use
Serif
Sans Serif
Decorative
Script

Requirements
Must have
• Black base wrap color
Nice to have
• Look at the mock up on the trash can photo with the little crabs. I think it would look cool on the wrap.
Should not have
• Our specialty is garlic Crabs. So we need to Highlight somewhere (The best crab in the bay)

```html
<!DOCTYPE html>
<html lang="en">
<head>
<meta charset="utf-8">
<title>Thibodeau Bayou – Truck Side Wrap</title>
<link href="https://fonts.googleapis.com/css2?family=Yellowtail&family=Alfa+Slab+One&family=Oswald:wght@700&family=Dancing+Script:wght@700&family=Libre+Caslon+Text&display=swap" rel="stylesheet">
<style>
  :root {
    --bg: #e4e4e4;
    --wrap-black: #141414;
    --lime-light: #d6ea6a;
    --lime: #a7c83a;
    --lime-deep: #5e8a1c;
    --pink: #d9546f;
    --gold: #d29a2a;
    --silver: #e8e8e8;
    --rust: #d8552b;
    --brick: #9b2a12;
    --crab-light: #f2a565;
    --crab-deep: #c5622c;
    --rule-grey: #bdbdbd;
  }
  html, body {
    margin: 0;
    width: 1200px;
    height: 600px;
    overflow: hidden;
    background: var(--bg);
  }
  .wrap-canvas { display: block; width: 1200px; height: 600px; }
  .wrap-panel { fill: var(--wrap-black); }
  .swoosh-green { fill: url(#limeFade); }
  .stripe-black { fill: none; stroke: var(--wrap-black); stroke-width: 16; }
  .stripe-pink { fill: none; stroke: var(--pink); stroke-width: 7; }
  .division-title { font-family: "Yellowtail", cursive; font-size: 44px; fill: var(--pink); }
  .brand-name { font-family: "Libre Caslon Text", serif; font-size: 30px; fill: var(--gold); letter-spacing: 1px; }
  .brand-dot { fill: var(--pink); }
  .contact-box { fill: var(--wrap-black); }
  .contact-url { font-family: "Libre Caslon Text", serif; font-size: 17px; fill: var(--gold); }
  .contact-phone { font-family: "Libre Caslon Text", serif; font-size: 24px; fill: var(--gold); }
  .specialty-arc { font-family: "Alfa Slab One", serif; font-size: 28px; fill: var(--gold); stroke: #5a3b06; stroke-width: 0.8; }
  .specialty-crab { font-family: "Oswald", sans-serif; font-weight: 700; font-size: 58px; fill: var(--silver); stroke: #6b6b6b; stroke-width: 1.5; }
  .gold-rule { stroke: var(--gold); stroke-width: 3; }
  .grey-rule { stroke: var(--rule-grey); stroke-width: 3; }
  .crab-art { fill: url(#crabTone); }
  .slogan-big { font-family: "Oswald", sans-serif; font-weight: 700; fill: var(--rust); stroke: #f3d3b8; stroke-width: 1.2; }
  .slogan-bay { fill: var(--brick); }
  .slogan-script { font-family: "Dancing Script", cursive; font-size: 30px; fill: var(--silver); stroke: #555; stroke-width: 0.8; }
</style>
</head>
<body>
<svg class="wrap-canvas" viewBox="0 0 1200 600" xmlns="http://www.w3.org/2000/svg">
  <defs>
    <linearGradient id="limeFade" x1="0" y1="0" x2="0" y2="1">
      <stop offset="0" stop-color="var(--lime-light)"/>
      <stop offset="0.5" stop-color="var(--lime)"/>
      <stop offset="1" stop-color="var(--lime-deep)"/>
    </linearGradient>
    <radialGradient id="crabTone" cx="0.5" cy="0.5" r="0.6">
      <stop offset="0" stop-color="var(--crab-light)"/>
      <stop offset="1" stop-color="var(--crab-deep)" stop-opacity="0.85"/>
    </radialGradient>
    <clipPath id="panelClip"><rect x="20" y="40" width="1160" height="520" rx="18"/></clipPath>
    <path id="specialtyCurve" d="M690,230 Q835,40 985,230"/>
  </defs>

  <g class="side-wrap" clip-path="url(#panelClip)">
    <rect class="wrap-panel" x="20" y="40" width="1160" height="520"/>
    <path class="swoosh-green" d="M20,340 C320,270 720,300 1180,190 L1180,560 L20,560 Z"/>
    <path class="stripe-pink" d="M20,335 C320,265 720,295 1180,186"/>
    <path class="stripe-black" d="M20,430 C360,320 760,340 1180,300"/>
    <path class="stripe-pink" d="M20,455 C360,345 760,365 1180,322"/>
    <path class="stripe-pink" d="M900,250 C1000,200 1100,150 1180,110"/>
  </g>

  <text class="division-title" x="110" y="125">Catering Division</text>

  <g class="brand-lockup">
    <circle class="brand-dot" cx="310" cy="205" r="10"/>
    <text class="brand-name" x="310" y="255" text-anchor="middle">THIBODEAU BAYOU</text>
  </g>

  <g class="contact-block">
    <rect class="contact-box" x="215" y="280" width="190" height="78" rx="6"/>
    <text class="contact-url" x="310" y="305" text-anchor="middle">THIBBAYOU.COM</text>
    <text class="contact-phone" x="310" y="340" text-anchor="middle">(707) 555-0148</text>
  </g>

  <g class="specialty">
    <text class="specialty-arc"><textPath href="#specialtyCurve" startOffset="50%" text-anchor="middle">Garlic Dungeness</textPath></text>
    <line class="gold-rule" x1="745" y1="192" x2="785" y2="192"/>
    <line class="gold-rule" x1="745" y1="204" x2="785" y2="204"/>
    <line class="gold-rule" x1="888" y1="192" x2="928" y2="192"/>
    <line class="gold-rule" x1="888" y1="204" x2="928" y2="204"/>
    <text class="specialty-crab" x="837" y="222" text-anchor="middle">CRAB</text>
  </g>

  <rect class="crab-art" x="770" y="240" width="190" height="285" rx="40" role="img" aria-label="Illustration of a cooked orange Dungeness crab"/>

  <g class="slogan">
    <line class="grey-rule" x1="1020" y1="110" x2="1150" y2="110"/>
    <line class="grey-rule" x1="1020" y1="120" x2="1150" y2="120"/>
    <text class="slogan-big" x="1085" y="178" font-size="56" text-anchor="middle">THE</text>
    <text class="slogan-big" x="1085" y="262" font-size="80" text-anchor="middle">BEST</text>
    <text class="slogan-script" x="1085" y="292" text-anchor="middle">in the</text>
    <text class="slogan-big slogan-bay" x="1085" y="378" font-size="80" text-anchor="middle">BAY</text>
    <line class="grey-rule" x1="1020" y1="400" x2="1150" y2="400"/>
    <line class="grey-rule" x1="1020" y1="410" x2="1150" y2="410"/>
  </g>
</svg>
</body>
</html>
```